Beautify our counselling web application

I have a web application in development and at the moment it is very plain.
It has being developed with laravel and vue. I need a simple design for the user interface to make it look more sleek and professional. I will need someone who is able to code the design as part of the service. The app is very low-cost for voluntary and social enterprise services and we don't have a lot of money so I need someone who is just starting out or someone with a big heart.
I have uploaded current pages to show the contents.
I will tip for good work.

Target Market(s)

Counsellors and psychotherapists

Industry/Entity Type

SaaS

Font styles to use
Serif
Sans Serif

Colors
0054AA
0677BA
7BADD7
CADEEF
E8F1F8

Requirements
Must have
• Ability to code the design into the current site
Nice to have
• elegant, modern. cool, profession. nice examples include brambleweft.com quillorbit.com fernovo.com
Should not have
• corny literal 90s icons, icons with more than one colour using primary colours

```html
<!DOCTYPE html>
<html lang="en">
<head>
<meta charset="utf-8">
<title>Counselling App – Screens</title>
<link href="https://fonts.googleapis.com/css2?family=Open+Sans:wght@400;600;700&display=swap" rel="stylesheet">
<style>
:root{
  --page:#ffffff;
  --surface:#f7f7f7;
  --card:#ffffff;
  --line:#e6e6e6;
  --ink:#222831;
  --muted:#8c8c8c;
  --navy:#2b3f66;
  --accent:#4353ff;
  --icon:#a9a9a9;
  --ok:#52c41a;
  --pill:#e8e8f2;
  --avatar-ring:#52c41a;
  --avatar-fill:#c9a48d;
}
*{box-sizing:border-box;margin:0;padding:0}
html,body{width:786px;height:1200px;overflow:hidden;background:var(--page)}
body{position:relative;font-family:"Open Sans",Arial,sans-serif;color:var(--ink)}
.screen{position:absolute;left:30px;width:719px;height:357px;background:var(--surface);box-shadow:0 1px 6px rgba(0,0,0,.08);overflow:hidden}
.screen--caseload{top:18px}
.screen--dashboard{top:406px}
.screen--client{top:794px}
.topbar{position:absolute;left:0;top:0;width:100%;height:37px;background:#fcfcfc;box-shadow:0 1px 2px rgba(0,0,0,.04)}
.avatar{position:absolute;left:23px;top:6.5px;width:24px;height:24px;border-radius:50%;border:1.5px solid var(--avatar-ring);background:radial-gradient(circle at 50% 45%,#d8b8a2,#8a6e5e)}
.app-name{position:absolute;right:83px;top:8px;font-size:14.5px;font-weight:700;color:var(--navy);letter-spacing:.1px}
.top-icons{position:absolute;left:651px;top:12.5px;display:flex;gap:5px}
.top-icons svg{width:12px;height:12px}
.sidebar{position:absolute;left:0;top:37px;width:126px;bottom:0;border-right:1px solid var(--line)}
.nav{list-style:none;position:absolute;left:21px;top:19px}
.nav li{height:23.2px;display:flex;align-items:center;font-size:8px;color:var(--ink)}
.nav li svg{width:10px;height:10px;margin-right:7px;fill:var(--icon)}
.nav li.is-active{color:var(--accent)}
.nav li.is-active svg{fill:var(--accent)}
.content{position:absolute;left:140px;top:37px;right:0;bottom:0}
.page-title{position:absolute;left:0;top:16px;font-size:17.5px;font-weight:700;color:var(--navy)}
.page-title .crumb{color:#b7b7b7}
/* caseload */
.searchbar{position:absolute;left:.5px;top:50px;width:339px;height:27px;background:var(--card);border-radius:3px;box-shadow:0 1px 3px rgba(0,0,0,.05);font-size:8px;color:var(--muted)}
.searchbar .filter{position:absolute;left:20px;top:8px}
.searchbar .divider{position:absolute;left:63.5px;top:2px;width:1px;height:23px;background:var(--line)}
.searchbar .search-icon{position:absolute;left:78px;top:8px;width:10px;height:10px}
.searchbar .placeholder{position:absolute;left:94px;top:8px}
.searchbar .clear{position:absolute;left:318px;top:9px;width:8px;height:8px}
.table{position:absolute;left:.5px;top:89px;width:555px;height:198px;background:var(--card);border-radius:3px;box-shadow:0 1px 3px rgba(0,0,0,.05);font-size:8px}
.row{display:grid;grid-template-columns:32.5px 41.5px 92px 41.5px 53.5px 73.5px 66px 74px auto;padding-left:14.5px;align-items:center;height:25.4px}
.row--head{height:27.5px;background:#fafafa;font-weight:600;color:var(--ink);margin-bottom:5px}
.dot{width:6px;height:6px;border-radius:50%;background:var(--ok);margin-left:5px}
.pill{display:inline-block;width:44px;height:15.5px;line-height:15.5px;text-align:center;background:var(--pill);color:var(--muted);border-radius:2px;margin-left:-7px}
/* dashboard */
.welcome{position:absolute;left:.5px;top:50px;width:553px;height:27px;background:#e4e4e4;border-radius:3px;font-size:8.5px;text-align:center;line-height:27px}
.section-title{position:absolute;left:0;font-size:11px;font-weight:700;color:var(--navy)}
.note{position:absolute;left:0;font-size:8px}
.btn-primary{position:absolute;left:.5px;top:119px;width:105px;height:20px;background:var(--accent);color:#fff;border-radius:2px;font-size:8px;font-weight:600;text-align:center;line-height:20px}
/* client workspace */
.tabs{position:absolute;left:0;top:46px;height:21px}
.tab{position:absolute;top:0;height:21px;border-radius:2px;font-size:8px;text-align:center;line-height:19px;border:1px solid var(--navy);color:var(--navy)}
.tab--workspace{left:.5px;width:70px;background:var(--accent);border-color:var(--accent);color:#fff}
.tab--info{left:79.5px;width:96px;background:var(--navy);color:#fff}
.tab--record{left:182.5px;width:79.5px}
.tab--progress{left:270.5px;width:83.5px}
.tab--payments{left:362.5px;width:65.5px;border-color:#c9c9c9;color:#bdbdbd}
.episode{position:absolute;left:.5px;top:89px;width:555px;height:197.5px;background:var(--card);border-radius:3px;box-shadow:0 1px 3px rgba(0,0,0,.05);font-size:8px}
.episode-head{height:27.5px;background:#fafafa;position:relative}
.episode-head .label{position:absolute;left:13.5px;top:8px}
.episode-head .started{position:absolute;right:107.5px;top:8px;color:#6b6b6b}
.episode-head .started b{font-weight:600;color:var(--ink)}
.episode-head .caret{position:absolute;left:454px;top:11px;width:6px;height:6px}
.btn-end{position:absolute;left:476px;top:5.5px;width:61.5px;height:15.5px;background:var(--accent);color:#fff;border-radius:2px;text-align:center;line-height:15.5px}
.modules{position:absolute;left:13.5px;top:45px;display:grid;grid-template-columns:repeat(6,85px);column-gap:4.2px;row-gap:5px}
.module{height:20px;border-radius:2px;color:#fff;text-align:center;line-height:20px;font-size:8px;font-weight:600}
.m-session{background:#d2637c}.m-assess{background:#b8763f}.m-risk{background:#b3a52c}
.m-treat{background:#55963a}.m-safe{background:#2f6b4e}.m-consent{background:#4a9ea0}
.m-quest{background:#4d6aa8}.m-doc{background:#4b3bb0}.m-note{background:#5c2e63}
.m-summary{background:#9d7a9f}.m-timeline{background:#8a3b8f}
</style>
</head>
<body>

<svg width="0" height="0" style="position:absolute">
  <defs>
    <symbol id="i-dash" viewBox="0 0 10 10"><rect x="0" y="0" width="10" height="3"/><rect x="0" y="4" width="4" height="6"/><rect x="5" y="4" width="5" height="2.5"/><rect x="5" y="7.5" width="5" height="2.5"/></symbol>
    <symbol id="i-pie" viewBox="0 0 10 10"><path d="M4.5 1A4.5 4.5 0 1 0 9 5.5H4.5Z"/><path d="M5.5 0V4.5H10A4.5 4.5 0 0 0 5.5 0Z"/></symbol>
    <symbol id="i-cal" viewBox="0 0 10 10"><path d="M0 1.5h10V10H0Z M1 4v5h8V4Z"/><rect x="2" y="5" width="1.5" height="1.2"/><rect x="4.3" y="5" width="1.5" height="1.2"/><rect x="6.6" y="5" width="1.5" height="1.2"/><rect x="2" y="7" width="1.5" height="1.2"/><rect x="4.3" y="7" width="1.5" height="1.2"/></symbol>
    <symbol id="i-pin" viewBox="0 0 10 10"><path d="M5 0A3.6 3.6 0 0 0 1.4 3.6C1.4 6.3 5 10 5 10S8.6 6.3 8.6 3.6A3.6 3.6 0 0 0 5 0Zm0 5a1.4 1.4 0 1 1 0-2.8A1.4 1.4 0 0 1 5 5Z"/></symbol>
    <symbol id="i-user" viewBox="0 0 10 10"><circle cx="5" cy="2.4" r="2.2"/><path d="M1.8 10V7a3.2 2.6 0 0 1 6.4 0v3Z"/></symbol>
    <symbol id="i-star" viewBox="0 0 10 10"><path d="M5 .4l1.4 3 3.3.4-2.4 2.3.6 3.3L5 7.8 2.1 9.4l.6-3.3L.3 3.8l3.3-.4Z"/></symbol>
    <symbol id="i-audit" viewBox="0 0 10 10"><path d="M4.2 0a4.2 4.2 0 1 0 2.6 7.5L9.2 10 10 9.2 7.5 6.8A4.2 4.2 0 0 0 4.2 0Zm0 1a3.2 3.2 0 1 1 0 6.4 3.2 3.2 0 0 1 0-6.4Z"/><rect x="2.6" y="4" width=".9" height="2"/><rect x="3.9" y="2.6" width=".9" height="3.4"/><rect x="5.2" y="3.4" width=".9" height="2.6"/></symbol>
    <symbol id="i-eye" viewBox="0 0 10 10"><path d="M5 2C2.4 2 .5 5 .5 5S2.4 8 5 8s4.5-3 4.5-3S7.6 2 5 2Zm0 5A2 2 0 1 1 5 3a2 2 0 0 1 0 4Z"/><circle cx="5" cy="5" r="1"/></symbol>
    <symbol id="i-tpl" viewBox="0 0 10 10"><path d="M0 0h10v3H0Zm1 1v1h8V1Z"/><path d="M0 4h4v6H0Zm1 1v4h2V5Z"/><rect x="5" y="4.3" width="5" height=".9"/><rect x="5" y="6.5" width="5" height=".9"/><rect x="5" y="8.7" width="5" height=".9"/></symbol>
    <symbol id="i-help" viewBox="0 0 12 12"><circle cx="6" cy="6" r="5.5" fill="#4353ff"/><path d="M4.4 4.6a1.6 1.6 0 1 1 2.4 1.4c-.5.3-.8.6-.8 1.2" stroke="#fff" stroke-width="1.1" fill="none"/><circle cx="6" cy="8.8" r=".7" fill="#fff"/></symbol>
    <symbol id="i-account" viewBox="0 0 12 12"><circle cx="6" cy="3" r="2.6" fill="#4353ff"/><path d="M2 12V9a4 3.2 0 0 1 8 0v3Z" fill="#4353ff"/></symbol>
    <symbol id="i-signin" viewBox="0 0 12 12"><path d="M6 1h5v10H6" stroke="#4353ff" stroke-width="1.1" fill="none"/><path d="M1 6h6.5M5 3.5 7.5 6 5 8.5" stroke="#4353ff" stroke-width="1.1" fill="none"/></symbol>
  </defs>
</svg>

<!-- Caseload -->
<section class="screen screen--caseload">
  <header class="topbar">
    <div class="avatar" role="img" aria-label="Profile photo of the signed-in counsellor"></div>
    <div class="app-name">Counselling App</div>
    <div class="top-icons"><svg><use href="#i-help"/></svg><svg><use href="#i-account"/></svg><svg><use href="#i-signin"/></svg></div>
  </header>
  <aside class="sidebar">
    <ul class="nav">
      <li><svg><use href="#i-dash"/></svg>Dashboard</li>
      <li class="is-active"><svg><use href="#i-pie"/></svg>Caseload</li>
      <li><svg><use href="#i-cal"/></svg>Calendar</li>
      <li><svg><use href="#i-pin"/></svg>Address Book</li>
      <li><svg><use href="#i-user"/></svg>Users</li>
      <li><svg><use href="#i-star"/></svg>Clients</li>
      <li><svg><use href="#i-audit"/></svg>Audit</li>
      <li><svg><use href="#i-eye"/></svg>Monitoring</li>
      <li><svg><use href="#i-tpl"/></svg>Templates</li>
    </ul>
  </aside>
  <main class="content">
    <h1 class="page-title">Caseload</h1>
    <div class="searchbar">
      <span class="filter">Filter ⌄</span>
      <span class="divider"></span>
      <svg class="search-icon" viewBox="0 0 10 10"><circle cx="4.2" cy="4.2" r="3.4" stroke="#999" fill="none"/><path d="M6.7 6.7 9.5 9.5" stroke="#999"/></svg>
      <span class="placeholder">Search</span>
      <svg class="clear" viewBox="0 0 8 8"><path d="M.5.5l7 7M7.5.5l-7 7" stroke="#999"/></svg>
    </div>
    <div class="table">
      <div class="row row--head"><span>Risk</span><span>Alerts</span><span>Clients</span><span>ID</span><span>Therapist</span><span>Date of referal</span><span>First Contact</span><span>Previous Episode</span><span>Contact</span></div>
      <div class="row"><span class="dot"></span><span></span><span>Peter Haynes</span><span>002</span><span>Paul</span><span>05/07/2022</span><span>20/09/2022</span><span></span><span><span class="pill">Total: 3</span></span></div>
      <div class="row"><span class="dot"></span><span></span><span>Roger Rowland</span><span>003</span><span>Paul</span><span>05/07/2022</span><span>20/09/2022</span><span></span><span><span class="pill">Total: 3</span></span></div>
      <div class="row"><span class="dot"></span><span></span><span>Rebecca Howes</span><span>004</span><span>Paul</span><span>05/07/2022</span><span>20/09/2022</span><span></span><span><span class="pill">Total: 3</span></span></div>
      <div class="row"><span class="dot"></span><span></span><span>Briony Beech</span><span>005</span><span>Mike</span><span>05/07/2022</span><span>20/09/2022</span><span></span><span><span class="pill">Total: 3</span></span></div>
      <div class="row"><span class="dot"></span><span></span><span>Bethany Josephs</span><span>006</span><span>Mike</span><span>05/07/2022</span><span>20/09/2022</span><span>20/11/2022</span><span><span class="pill">Total: 3</span></span></div>
      <div class="row"><span class="dot"></span><span></span><span>Sarsh Buckingham</span><span>007</span><span>Mike</span><span>05/07/2022</span><span>20/09/2022</span><span></span><span><span class="pill">Total: 3</span></span></div>
    </div>
  </main>
</section>

<!-- Dashboard -->
<section class="screen screen--dashboard">
  <header class="topbar">
    <div class="avatar" role="img" aria-label="Profile photo of the signed-in counsellor"></div>
    <div class="app-name">Counselling App</div>
    <div class="top-icons"><svg><use href="#i-help"/></svg><svg><use href="#i-account"/></svg><svg><use href="#i-signin"/></svg></div>
  </header>
  <aside class="sidebar">
    <ul class="nav">
      <li class="is-active"><svg><use href="#i-dash"/></svg>Dashboard</li>
      <li><svg><use href="#i-pie"/></svg>Caseload</li>
      <li><svg><use href="#i-cal"/></svg>Calendar</li>
      <li><svg><use href="#i-pin"/></svg>Address Book</li>
      <li><svg><use href="#i-user"/></svg>Users</li>
      <li><svg><use href="#i-star"/></svg>Clients</li>
      <li><svg><use href="#i-audit"/></svg>Audit</li>
      <li><svg><use href="#i-eye"/></svg>Monitoring</li>
      <li><svg><use href="#i-tpl"/></svg>Templates</li>
    </ul>
  </aside>
  <main class="content">
    <h1 class="page-title">Dashboard</h1>
    <div class="welcome">Welcome to Demo</div>
    <h2 class="section-title" style="top:96px">Notifications</h2>
    <div class="btn-primary">Create notification</div>
    <p class="note" style="top:152px">No notifications</p>
    <h2 class="section-title" style="top:176px">Today</h2>
    <p class="note" style="top:193px">No appointments</p>
    <h2 class="section-title" style="top:215px">Reviews</h2>
    <p class="note" style="top:232.5px">No reviews!</p>
  </main>
</section>

<!-- Client workspace -->
<section class="screen screen--client">
  <header class="topbar">
    <div class="avatar" role="img" aria-label="Profile photo of the signed-in counsellor"></div>
    <div class="app-name">Counselling App</div>
    <div class="top-icons"><svg><use href="#i-help"/></svg><svg><use href="#i-account"/></svg><svg><use href="#i-signin"/></svg></div>
  </header>
  <aside class="sidebar">
    <ul class="nav">
      <li><svg><use href="#i-dash"/></svg>Dashboard</li>
      <li class="is-active"><svg><use href="#i-pie"/></svg>Caseload</li>
      <li><svg><use href="#i-cal"/></svg>Calendar</li>
      <li><svg><use href="#i-pin"/></svg>Address Book</li>
      <li><svg><use href="#i-user"/></svg>Users</li>
      <li><svg><use href="#i-star"/></svg>Clients</li>
      <li><svg><use href="#i-audit"/></svg>Audit</li>
      <li><svg><use href="#i-eye"/></svg>Monitoring</li>
      <li><svg><use href="#i-tpl"/></svg>Templates</li>
    </ul>
  </aside>
  <main class="content">
    <h1 class="page-title"><span class="crumb">Caseload/ </span>Peter Hynes</h1>
    <nav class="tabs">
      <span class="tab tab--workspace">Workspace</span>
      <span class="tab tab--info">Client information</span>
      <span class="tab tab--record">Client record</span>
      <span class="tab tab--progress">Client progress</span>
      <span class="tab tab--payments">Payments</span>
    </nav>
    <div class="episode">
      <div class="episode-head">
        <span class="label">Episode 1</span>
        <span class="started"><b>Started:</b> Wed Sep 14, 2022</span>
        <svg class="caret" viewBox="0 0 6 6"><path d="M1 4 3 2 5 4" stroke="#777" fill="none"/></svg>
        <span class="btn-end">End episode</span>
      </div>
      <div class="modules">
        <span class="module m-session">Session Record</span>
        <span class="module m-assess">Assessment</span>
        <span class="module m-risk">Risk management</span>
        <span class="module m-treat">Treatment plan</span>
        <span class="module m-safe">Safeguarding</span>
        <span class="module m-consent">Consent</span>
        <span class="module m-quest">Questionnaire</span>
        <span class="module m-doc">Document</span>
        <span class="module m-note">Non-clinical note</span>
        <span class="module m-summary">Summary</span>
        <span class="module m-timeline">Timeline</span>
      </div>
    </div>
  </main>
</section>

</body>
</html>
```